Popup Banners - BrightCounsel - Legal Technology

- We need two banners (same style) designed with two different images and different text.

- The details of the printing requirements are attached, along with suggested images.

- The banners should share the same theme as our website www.brightcounsel.com.au

- The first banner would include our logo (attached), use the 'roads join' image (attached) in some way and text: New Opportunities - Where legal services and technology meet.

- The second banner would include our logo (attached), use the 'jigsaw' image (attached) in some way and use text: Legal Technology Strategy, Advice and Capability.

- Details on what are required from the Printer is attached also.

Target Market(s)

Legal Professionals

Industry/Entity Type

Information Technology

Font styles to use
Sans Serif

Requirements
Must have
• Our logo (attached), suggested text and the image mentioned for each.
Nice to have
• Professional and modern look
Should not have
• Cheap looking

```html
<!DOCTYPE html>
<html lang="en">
<head>
<meta charset="utf-8">
<title>BrightCounsel – Popup Banners</title>
<link href="https://fonts.googleapis.com/css2?family=Oswald:wght@200;300;400&display=swap" rel="stylesheet">
<style>
  :root {
    --page-bg: #f1f1f1;
    --sky-blue: #0a6fb0;
    --sky-light: #4c98cf;
    --field-green: #5e8f2c;
    --field-dark: #3f6a1c;
    --navy: #1a2f50;
    --navy-deep: #12233d;
    --glow-blue: #9cc9f0;
    --accent-blue: #5aa8e6;
    --white: #ffffff;
    --footer-grey: #e1e1e1;
    --logo-ink: #4a4543;
  }
  * { margin: 0; padding: 0; box-sizing: border-box; }
  html, body { width: 1200px; height: 1200px; overflow: hidden; }
  body {
    background: var(--page-bg);
    font-family: "Oswald", "Arial Narrow", sans-serif;
    position: relative;
  }
  .banner {
    position: absolute;
    top: 114px;
    width: 397px;
    height: 971px;
    overflow: hidden;
  }
  .banner--opportunities { left: 153px; }
  .banner--strategy { left: 650px; background: var(--navy); }

  .banner__visual {
    position: absolute;
    left: 0; top: 0;
    width: 100%;
    height: 816px;
  }
  .banner--opportunities .banner__visual {
    background: linear-gradient(180deg,
      var(--sky-blue) 0%, var(--sky-blue) 40%,
      var(--sky-light) 52%, var(--field-green) 56%,
      var(--field-green) 75%, var(--field-dark) 100%);
  }
  .banner--strategy .banner__visual {
    background:
      radial-gradient(circle at 78% 76%, var(--glow-blue) 0%, #3f6fa3 18%, transparent 42%),
      linear-gradient(180deg, var(--navy) 0%, var(--navy) 58%, var(--navy-deep) 100%);
  }

  .banner__headline {
    position: absolute;
    left: 0; right: 0;
    text-align: center;
    color: var(--white);
    font-weight: 200;
    text-transform: uppercase;
    line-height: 1;
  }
  .banner--opportunities .banner__headline { top: 68px; }
  .headline__lead { display: block; font-size: 58px; letter-spacing: -0.5px; }
  .headline__main { display: block; font-size: 58px; letter-spacing: -1px; margin-top: 4px; }
  .headline__sub { display: block; font-size: 34px; line-height: 1.12; letter-spacing: -0.5px; margin-top: 6px; }

  .banner--strategy .banner__headline { top: 76px; }
  .headline__kicker { display: block; font-size: 42px; letter-spacing: -0.5px; }
  .headline__term {
    display: block;
    font-size: 74px;
    color: var(--accent-blue);
    letter-spacing: -1px;
    line-height: 1.03;
  }
  .headline__term--first { margin-top: 8px; }
  .headline__amp { display: block; font-size: 58px; line-height: 1.2; }

  .banner__footer {
    position: absolute;
    left: 0; bottom: 0;
    width: 100%;
    height: 155px;
    display: flex;
    align-items: center;
    justify-content: center;
    gap: 18px;
  }
  .banner--opportunities .banner__footer { background: var(--footer-grey); }
  .banner--strategy .banner__footer { background: var(--white); }

  .banner__notch {
    position: absolute;
    top: -1px;
    left: 170px;
    width: 40px;
    height: 18px;
  }

  .brand__mark {
    width: 26px;
    height: 26px;
    background: var(--accent-blue);
  }
  .brand__name {
    font-size: 30px;
    font-weight: 400;
    letter-spacing: 0.2em;
    color: var(--logo-ink);
  }
</style>
</head>
<body>

  <section class="banner banner--opportunities">
    <div class="banner__visual" role="img" aria-label="Photo of two dirt roads joining on a green grassy hill under a blue sky"></div>
    <h1 class="banner__headline">
      <span class="headline__lead">New</span>
      <span class="headline__main">Opportunities</span>
      <span class="headline__sub">Where legal services<br>and technology come<br>together</span>
    </h1>
    <footer class="banner__footer">
      <svg class="banner__notch" viewBox="0 0 40 18" aria-hidden="true">
        <polygon points="0,0 40,0 20,18" fill="#3f6a1c"/>
      </svg>
      <span class="brand__mark" aria-hidden="true"></span>
      <span class="brand__name">BrightCounsel</span>
    </footer>
  </section>

  <section class="banner banner--strategy">
    <div class="banner__visual" role="img" aria-label="Photo of a hand placing a glowing jigsaw puzzle piece on a dark blue puzzle"></div>
    <h1 class="banner__headline">
      <span class="headline__kicker">Legal Technology</span>
      <span class="headline__term headline__term--first">Strategy</span>
      <span class="headline__term">Advice</span>
      <span class="headline__amp">&amp;</span>
      <span class="headline__term">Capability</span>
    </h1>
    <footer class="banner__footer">
      <svg class="banner__notch" viewBox="0 0 40 18" aria-hidden="true">
        <polygon points="0,0 40,0 20,18" fill="#12233d"/>
      </svg>
      <span class="brand__mark" aria-hidden="true"></span>
      <span class="brand__name">BrightCounsel</span>
    </footer>
  </section>

</body>
</html>
```